Start-Up Property Development Company Requires Word Press Website Design

A new property development company in Sydney requires a new website.
This version (Version 1) is very simple and will represent one, small aspect of what the company does, which is acquiring properties for redevelopment:

Needed:
- 1 page incorporating copy, logo and illustration.
- Email contact form.
- Contact information.

It will be expanded in the next few months to include another section for marketing homes for sale (Version 2). This section should sit on top of the Version 1 (in the top section of the same scrolling page).

So this initial design must be able to simply incorporate the expansion.

The site design needs to:
- Take up the entire width of the monitor.
- Not be too different from companies corporate look and feel.
- Be simple, functional and elegant.
- Have a long scroll (1 page) with navigation items at the top of the screen simply linking to the corresponding section lower in the page.

Reason: Not happy with the choice of designs. I'm wanting something clean and fresh and not too intensive with graphics.

```html
<!DOCTYPE html>
<html lang="en">
<head>
<meta charset="utf-8">
<title>Norvale Property</title>
<link rel="stylesheet" href="https://fonts.googleapis.com/css2?family=Arimo:wght@400;700&family=Lato:wght@400;700&display=swap">
<style>
  :root {
    --red: #c4202a;
    --ink: #1c1c1c;
    --text: #4a4a4a;
    --muted: #6a6a6a;
    --line: #e4e4e4;
    --footer: #231f20;
    --white: #ffffff;
  }
  * { margin: 0; padding: 0; box-sizing: border-box; }
  html, body { width: 1200px; height: 2426px; overflow: hidden; background: var(--white); }
  body { position: relative; font-family: "Lato", "Helvetica Neue", sans-serif; color: var(--text); }
  .abs { position: absolute; }

  /* Header */
  .brand { left: 107px; top: 24px; display: flex; align-items: center; gap: 12px; }
  .brand-mark { width: 22px; height: 22px; background: var(--red); }
  .brand-name { font-family: "Arimo", Arial, sans-serif; font-weight: 700; color: var(--ink); font-size: 28px; line-height: 30px; letter-spacing: 0.5px; }
  .brand-name span { display: block; font-size: 24px; letter-spacing: 1px; padding-left: 26px; }
  .nav { top: 44px; left: 496px; width: 596px; display: flex; justify-content: space-between; list-style: none; font-size: 12.5px; color: var(--ink); letter-spacing: 0.3px; }
  .nav li { position: relative; }
  .nav .active { color: var(--red); }
  .nav .active::after { content: ""; position: absolute; left: 0; right: -6px; top: 25px; height: 3px; background: var(--red); }
  .nav .active::before { content: ""; position: absolute; left: 50%; top: 27px; margin-left: -2px; border: 5px solid transparent; border-top-color: var(--red); }

  /* Hero */
  .hero { left: 107px; top: 120px; width: 985px; height: 482px; overflow: hidden;
    background: linear-gradient(90deg, #3f6f9a 0%, #5b87ad 30%, #b9c8d4 52%, #dfe4e8 70%, #9aa3a8 100%); }
  .hero-shade { position: absolute; inset: auto 0 0 0; height: 55%; background: linear-gradient(180deg, rgba(40,60,80,0) 0%, rgba(90,100,110,0.45) 100%); }
  .hero-title { left: 22px; top: 82px; font-family: "Arimo", Arial, sans-serif; font-weight: 700; font-size: 44px; color: var(--white); letter-spacing: 0.5px; }
  .hero-text { left: 22px; top: 140px; width: 490px; font-size: 16.5px; line-height: 29px; color: var(--white); }
  .hero-dots { left: 22px; top: 418px; display: flex; gap: 4px; }
  .hero-dots i { width: 10px; height: 10px; border-radius: 50%; background: var(--white); }
  .hero-dots i:first-child { background: var(--red); }

  /* Section headings */
  .heading { font-family: "Arimo", Arial, sans-serif; font-weight: 700; font-size: 23px; color: var(--ink); }
  .rule { height: 3px; width: 76px; background: var(--red); }
  .copy { font-size: 14px; line-height: 24.5px; color: var(--text); }
  .btn { display: flex; align-items: center; justify-content: center; width: 129px; height: 46px; background: var(--red); color: var(--white); font-size: 17px; }

  .frame { width: 474px; height: 262px; border: 2px solid #efefef; }
  .frame .photo { position: absolute; left: 20px; top: 17px; width: 432px; height: 224px; }
  .photo-commercial { background: linear-gradient(180deg, #2f4f86 0%, #6f86a8 40%, #c9b08a 65%, #3b4a33 85%, #3d7db0 100%); }
  .photo-residential { background: linear-gradient(180deg, #7a746c 0%, #d9d0bd 35%, #f2ede4 60%, #b7aca0 100%); }

  /* Search band */
  .band { left: 0; top: 1211px; width: 1200px; height: 151px; background: var(--red); }
  .band-title { left: 107px; top: 28px; font-family: "Arimo", Arial, sans-serif; font-weight: 700; font-size: 22px; color: var(--white); }
  .band-text { left: 107px; top: 70px; width: 820px; font-size: 13.5px; line-height: 24px; color: var(--white); }
  .band-btn { left: 962px; top: 52px; width: 129px; height: 45px; border: 2px solid var(--white); color: var(--white); font-size: 16px; display: flex; align-items: center; justify-content: center; }

  /* Properties */
  .tile { top: 1556px; width: 300px; height: 231px; }
  .tile-1 { left: 107px; background: linear-gradient(180deg, #d8d4cc 0%, #eeeae3 45%, #8a5a3a 80%, #6e442a 100%); }
  .tile-2 { left: 450px; background: linear-gradient(180deg, #1d3c8a 0%, #2f4f9c 45%, #2b2420 65%, #3a3d22 100%); }
  .tile-3 { left: 792px; background: linear-gradient(180deg, #5a5250 0%, #7b716d 50%, #5e5753 100%); }
  .tile-caption { top: 1818px; font-family: "Arimo", Arial, sans-serif; font-weight: 700; font-size: 16.5px; color: var(--red); }
  .tile-search { position: absolute; left: 133px; top: 98px; }

  .portrait { left: 906px; top: 1908px; width: 172px; height: 180px; background: linear-gradient(180deg, #ffffff 0%, #f1e6dc 30%, #a46c45 60%, #2a2626 100%); }

  /* Footer */
  .footer { left: 0; top: 2236px; width: 1200px; height: 190px; background: var(--footer); }
  .footer-brand { left: 107px; top: 30px; font-family: "Arimo", Arial, sans-serif; font-weight: 700; color: #d9d9d9; font-size: 38px; line-height: 40px; letter-spacing: 1px; }
  .footer-brand span { display: block; font-size: 31px; padding-left: 40px; }
  .footer-links { right: 108px; top: 34px; display: flex; gap: 18px; font-size: 13.5px; color: #d6d6d6; }
  .footer-links b { font-weight: 400; }
  .social { right: 108px; top: 94px; display: flex; gap: 12px; }
  .social i { width: 29px; height: 29px; border-radius: 50%; background: #3d393a; }
  .copyright { left: 107px; top: 143px; font-size: 13.5px; color: #d6d6d6; }
</style>
</head>
<body>
  <header>
    <div class="abs brand"><i class="brand-mark"></i><div class="brand-name">NORVALE<span>PROPERTY</span></div></div>
    <ul class="abs nav">
      <li class="active">HOME</li>
      <li>ABOUT US</li>
      <li>WHAT WE DO</li>
      <li>PROPERTIES</li>
      <li>BLOG</li>
      <li>CONTACT US</li>
    </ul>
  </header>

  <section class="abs hero">
    <div role="img" aria-label="Modern white villa with an infinity pool overlooking the ocean" style="position:absolute;inset:0;"></div>
    <div class="hero-shade"></div>
    <h1 class="abs hero-title">NORVALE PROPERTY</h1>
    <p class="abs hero-text">Norvale Property is property development company located in Sydney. We are currently searching for properties to acquire and redevelop.</p>
    <div class="abs hero-dots"><i></i><i></i><i></i><i></i></div>
  </section>

  <section class="development">
    <h2 class="abs heading" style="left:107px;top:647px;">COMMERCIAL DEVELOPMENT</h2>
    <div class="abs rule" style="left:107px;top:688px;"></div>
    <div class="abs frame" style="left:107px;top:729px;"><div class="photo photo-commercial" role="img" aria-label="Commercial building with palm trees and pool at dusk"></div></div>
    <p class="abs copy" style="left:107px;top:1012px;width:474px;">Lorem ipsum dolor sit amet, nec ludus minimum luptatum ad, choro erroribus interpretaris has et. Eam ad delenit forensibus, ut nec rebum eirmod iuvaret, vis in consetetur persequeris.</p>
    <div class="abs btn" style="left:107px;top:1111px;">More Info</div>

    <h2 class="abs heading" style="left:618px;top:647px;">RESIDENTIAL DEVELOPMENT</h2>
    <div class="abs rule" style="left:618px;top:688px;"></div>
    <div class="abs frame" style="left:618px;top:729px;"><div class="photo photo-residential" role="img" aria-label="Bright living room with white sofa and gold curtains"></div></div>
    <p class="abs copy" style="left:618px;top:1012px;width:474px;">Lorem ipsum dolor sit amet, nec ludus minimum luptatum ad, choro erroribus interpretaris has et. Eam ad delenit forensibus, ut nec rebum eirmod iuvaret, vis in consetetur persequeris.</p>
    <div class="abs btn" style="left:618px;top:1111px;">More Info</div>
  </section>

  <section class="abs band">
    <h2 class="abs band-title">SEARCH PROPERTY</h2>
    <p class="abs band-text">An mea nusquam temporibus, congue essent tibique ex vix. Te diam audiam electram ius, qui no vocibus assentior.An mea nusquam temporibus, congue essent tibique ex vix. Te diam audiam electram ius, qui no vocibus assentior.</p>
    <div class="abs band-btn">Search</div>
  </section>

  <section class="properties">
    <h2 class="abs heading" style="left:107px;top:1420px;">OUR PROPERTIES</h2>
    <div class="abs rule" style="left:107px;top:1459px;"></div>
    <p class="abs copy" style="left:107px;top:1485px;width:985px;">Lorem ipsum dolor sit amet, nec ludus minimum luptatum ad, choro erroribus interpretaris has et. Eam ad delenit forensibus, ut nec rebum eirmod iuvaret, vis in consetetur persequeris. Lorem ipsum dolor sit amet, nec ludus minimum luptatum ad, choro erroribus interpretaris has et.</p>
    <div class="abs tile tile-1" role="img" aria-label="Open-plan living room with timber floors"></div>
    <div class="abs tile tile-2" role="img" aria-label="Modern dark house lit up at night"></div>
    <div class="abs tile tile-3" role="img" aria-label="Elegant living room interior">
      <svg class="tile-search" width="34" height="34" viewBox="0 0 34 34"><circle cx="13" cy="13" r="10" fill="none" stroke="#fff" stroke-width="4"/><line x1="20.5" y1="20.5" x2="31" y2="31" stroke="#fff" stroke-width="5" stroke-linecap="round"/></svg>
    </div>
    <h3 class="abs tile-caption" style="left:107px;">LOREUM IPSUM DOLOR</h3>
    <h3 class="abs tile-caption" style="left:450px;">LOREUM IPSUM DOLOR</h3>
    <h3 class="abs tile-caption" style="left:792px;">LOREUM IPSUM DOLOR</h3>
  </section>

  <section class="about">
    <h2 class="abs heading" style="left:107px;top:1890px;">SHORTLY ABOUT US</h2>
    <div class="abs rule" style="left:107px;top:1930px;"></div>
    <p class="abs copy" style="left:107px;top:1955px;width:800px;">No per zril prompta ullamcorper. Ex soluta blandit vis, mei vitae urbanitas an, ei altera apeirian insolens duo. His inductum imperdiet ea, ius ad virtute posidonium. Sit in eligendi necessitatibus, eos an evertitur delicatissimi. Viderer postulant mea et. An agam ocurreret laboramus vis.</p>
    <p class="abs copy" style="left:107px;top:2045px;width:790px;">No per zril prompta ullamcorper. Ex soluta blandit vis, mei vitae urbanitas an, ei altera apeirian insolens duo. His inductum imperdiet ea, ius ad virtute posidonium. Sit in eligendi necessitatibus, eos an evertitur delicatissimi.</p>
    <div class="abs portrait" role="img" aria-label="Portrait of a company representative"></div>
    <div class="abs btn" style="left:107px;top:2117px;">More Info</div>
  </section>

  <footer class="abs footer">
    <div class="abs footer-brand">NORVALE<span>PROPERTY</span></div>
    <div class="abs footer-links"><span>Terms Of Use</span><b>/</b><span>Privacy Policy</span><b>/</b><span>Site Map</span></div>
    <div class="abs social" aria-label="Social links"><i></i><i></i><i></i><i></i><i></i></div>
    <p class="abs copyright">Copyright @ 2014 Norvale Property.All Rights Reserved.</p>
  </footer>
</body>
</html>
```